Design and Renovation Company Luxury Business Card

I want to create a luxury business card for a Design and Renovation Firm . We will use our current logo. The company name is 742BUILD. We do not want anything standard. We need a very unique concept.
Please see uploaded inspiration. I really like the textured paper option. I would like the card to be thick with debossing, and/or embossing options. The logo has orange in it but I would like to see the card with and without the orange. I think the orange may make the company feel less high-end. The goal is to elevate the logo not match its vibe per se of the logo. We want something very unique, not standard at all!
I would like a space for :
Logo,
Name,
Position,
Email,
Office number,
Website Address,
Business Address,
Thank you!
Have fun!
Target Market(s)
Home owners Age 35 +
Industry/Entity Type
Design and Renovation
Contact Information for Business Card
Logo, Name, Position, Email, Office number, Website Address, Business Address,.
Colors
Designer to choose colors to be used in the design.
Requirements
Must have
- A luxury designer feel. Must be black or dark grey but open to other luxury ideas.
Nice to have
- Gold, silver, black embossing or debossing. Textured paper design.
Should not have
- A cheap look and feel.

```html
<!DOCTYPE html>
<html lang="en">
<head>
<meta charset="utf-8">
<title>742BUILD Business Card</title>
<link rel="stylesheet" href="https://fonts.googleapis.com/css2?family=PT+Sans:wght@400;700&display=swap">
<style>
  :root {
    --stage: #cccccc;
    --umber: #5b5142;
    --umber-lattice: #63594a;
    --paper: #ffffff;
    --paper-lattice: #f5f3ec;
    --accent: #f7913a;
    --ink: #1c1a18;
    --light: #ffffff;
  }
  * { margin: 0; padding: 0; box-sizing: border-box; }
  html, body {
    width: 1200px;
    height: 1112px;
    overflow: hidden;
    background: var(--stage);
    font-family: "PT Sans", sans-serif;
  }
  .card {
    position: absolute;
    width: 753px;
    height: 443px;
    overflow: hidden;
  }
  .card-front { left: 75px; top: 75px; background: var(--umber); }
  .card-back { left: 372px; top: 593px; background: var(--paper); }
  .texture { position: absolute; left: 0; top: 0; }

  .brand {
    position: absolute;
    left: 310px;
    top: 333px;
    display: flex;
    align-items: center;
    gap: 24px;
  }
  .brand-mark {
    width: 28px;
    height: 28px;
    background: var(--accent);
  }
  .brand-name {
    font-size: 74px;
    font-weight: 400;
    letter-spacing: 3px;
    line-height: 1;
    color: var(--light);
  }

  .holder-name {
    position: absolute;
    left: 45px;
    top: 62px;
    font-size: 46px;
    font-weight: 700;
    line-height: 1;
    color: var(--umber);
  }
  .holder-role {
    position: absolute;
    left: 46px;
    top: 116px;
    font-size: 21px;
    font-weight: 700;
    letter-spacing: 3.2px;
    line-height: 1;
    color: var(--accent);
  }
  .contact-list {
    position: absolute;
    left: 46px;
    top: 256px;
    list-style: none;
    font-size: 21px;
    line-height: 38px;
    color: var(--ink);
  }
  .contact-list li::before { content: "- "; }
</style>
</head>
<body>
  <section class="card card-front">
    <svg class="texture" width="753" height="443" role="img" aria-label="Diagonal lattice texture along the left edge of the card">
      <polygon points="0,0 172,0 350,178 86,443 0,443" fill="var(--umber-lattice)"/>
    </svg>
    <div class="brand">
      <span class="brand-mark"></span>
      <span class="brand-name">742BUILD</span>
    </div>
  </section>

  <section class="card card-back">
    <svg class="texture" width="753" height="443" role="img" aria-label="Faint diagonal lattice texture in the upper right corner">
      <polygon points="498,0 753,0 753,400 428,73" fill="var(--paper-lattice)"/>
    </svg>
    <h1 class="holder-name">YOUR NAME</h1>
    <p class="holder-role">COMPANY MANAGER</p>
    <ul class="contact-list">
      <li>(905) 555-0142</li>
      <li>18 Harbour Crest Drive Oakville, Ontario Canada L6K 2B4</li>
      <li>info@742build.com</li>
      <li>www.742build.ca</li>
    </ul>
  </section>
</body>
</html>
```